Website design for an Online pastry shop

Website Name : www.lanternandplum.com

Description of the website and its target audience
We are a premium pastry company producing delicious cakes, macarons, cookies, gelato, and other sweet dessert. Our differentiation is that our products are freshly produced with premium quality imported ingredients and one bite into our products set us apart from other bakery shop. We online retail online so as to provide high quality products at a affordable cost. Our products has received raving reviews by many food enthusiast even the hard to please ones. The products contain more natural ingredients and we do not add preservatives. The return rates for our pastry is almost 80%. You only need to try once to be return customers. Our greatest challenge is getting customer to take the first bite. We are so sure of our products that we are going to give people free food tasting.

We are based in China but all our products are developed by award winning chefs from 5 stars hotel. The target customer is woman 16 to 40+ in china. Working class ladies and demand high quality products. A modern, sophisticated and minimalist website

This is a competitive market and image is crucial for such a food ‘conscious ’ orientated customer. They want to feel that they are buying from a reliable company that take great effort to ensure food cleaniness and safety yet affordable price. We make almost 98% of sub ingredients ourselves and we make it by hand.

Style/theme ideas for the web page design
I am looking for a elegant a little rustic, handmade feel yet sophisticated design - one that is easy to the eye yet functional and easy for the user to navigate through. Good play of fonts to give let it feel unique and customised. Black and white is our corporate colours. However, we do not want black background as it does not tease the taste bud. All our colours should come from our products. Customers should be very close to our products. They eat with their eyes first. Black and white is just accent.

Inspirational and competitors websites
http://www.47torte.com/ ( Key competitor )
I like the simple, clean look. The products are the key focus
https://www.pleemo.com/
clean, fresh and different. Attractive with purpose. Feminine
http://quillandbobbin.com/
this has a great layout - lots of information and nicely presented. Very sweet and feminine
http://www.storehavenrow.com/
product features is the focus
http://www.odettevulmers.com/store/
fun, feminine, rustic

Number of pages needed : 6 ( Uncoded PSD design only )
Page descriptions
Home Page - This page will show what makes our products stand out from the competitors and provide an introduction of who we are.
2nd page : Product catalogue
3nd page: Detail Product page with pictures and descriptions. Select products size and add to cart....
4rd page: Brand Story with pictures and descriptions.
5th page Contact Us : Here they can contact or schedule an appointment for free product tasting
6th page : Check out page

Target Market(s)

Female, Asian, Working Class, Office

Industry/Entity Type

Shop

Number of Pages Required

5+ page

Font styles to use
Other font styles liked:
• See packaging

Requirements
Must have
• Please see the project wire frame file " main page.png " or file number 70

```html
<!DOCTYPE html>
<html lang="en">
<head>
<meta charset="utf-8">
<title>Lantern &amp; Plum — Premium Pastry</title>
<link rel="stylesheet" href="https://fonts.googleapis.com/css2?family=Montserrat:wght@400;600;700&family=Open+Sans:wght@400;600&family=Playfair+Display:ital,wght@0,400;1,400&display=swap">
<style>
:root{
  --ink:#1d1d1d;
  --text:#5a5a5a;
  --muted:#9a9a9a;
  --rule:#e4e4e4;
  --pink:#e7336c;
  --mint:#a7d6cc;
  --mint-deep:#86bfb3;
  --footer:#1c1c1c;
  --footer-text:#b5b5b5;
  --white:#ffffff;
}
*{box-sizing:border-box;margin:0;padding:0}
html,body{width:1200px;height:2512px;overflow:hidden;background:var(--white)}
body{position:relative;font-family:"Open Sans",Arial,sans-serif;color:var(--text)}
.abs{position:absolute}
.center{text-align:center}

/* header */
.delivery-tag{left:170px;top:61px;width:210px;height:42px;background:var(--mint);border:2px solid var(--ink);display:flex;align-items:center;justify-content:center;font:700 13px "Montserrat",sans-serif;letter-spacing:3px;color:var(--ink)}
.delivery-note{left:170px;top:108px;width:210px;font-size:11px;color:var(--ink)}
.brand-mark{left:557px;top:20px;width:86px;height:86px;border-radius:50%;background:var(--ink)}
.brand-name{left:450px;top:112px;width:300px;font:400 21px "Montserrat",sans-serif;color:var(--ink)}
.call{left:870px;top:20px;font-size:14px;color:var(--ink)}
.search{left:1012px;top:19px}
.login{left:800px;top:66px;width:66px;height:34px;border:2px solid var(--ink);font:700 11px "Montserrat",sans-serif;letter-spacing:1px;display:flex;align-items:center;justify-content:center;color:var(--ink)}
.signup{left:880px;top:76px;font:700 11px "Montserrat",sans-serif;letter-spacing:1px;color:var(--ink)}
.cart{left:952px;top:72px;display:flex;align-items:center;gap:6px;font:700 11px "Montserrat",sans-serif;letter-spacing:1px;color:var(--ink)}
.cart .count{width:18px;height:18px;border-radius:50%;background:var(--pink);color:#fff;font-size:10px;display:flex;align-items:center;justify-content:center;letter-spacing:0}
.main-nav{left:0;top:190px;width:1200px;display:flex;justify-content:center;gap:14px;font:400 14px "Montserrat",sans-serif;letter-spacing:1px;color:var(--text)}
.main-nav .sep{color:var(--muted)}
.main-nav .active{color:var(--ink);font-weight:600}
.nav-rule{left:0;top:229px;width:1200px;height:1px;background:var(--rule)}

/* hero */
.hero{left:0;top:234px;width:1200px;height:497px;background:linear-gradient(100deg,#f6f1f2 0%,#fbf7f8 40%,#f3e9ec 70%,#ead8de 100%)}
.hero-tart{left:690px;top:390px;width:480px;height:280px;border-radius:50% 50% 46% 46%;background:radial-gradient(ellipse at 50% 35%,#f4f0f1 0%,#ddcfd6 45%,#b7825a 80%,#9a6540 100%)}
.hero-kicker{left:450px;top:285px;width:300px;font:600 12px "Montserrat",sans-serif;letter-spacing:5px;color:var(--text)}
.hero-title{left:450px;top:304px;width:300px;font:400 28px "Montserrat",sans-serif;letter-spacing:6px;color:var(--ink)}
.hero-sub{left:450px;top:343px;width:300px;font-size:12px;color:var(--muted)}
.hero-badge{left:488px;top:378px;width:224px;height:224px;border-radius:50%;background:var(--mint);border:4px dashed #ffffff;display:flex;flex-direction:column;align-items:center;justify-content:center;color:var(--ink)}
.hero-badge .b-top{font:600 13px "Montserrat",sans-serif;letter-spacing:5px}
.hero-badge .b-script{font:italic 400 30px "Playfair Display",serif;line-height:36px;color:var(--pink)}
.hero-badge .b-main{font:700 40px "Montserrat",sans-serif;letter-spacing:2px;line-height:44px}
.hero-badge .b-sub{margin-top:6px;font-size:11px;color:var(--text)}
.hero-foot{left:420px;top:615px;width:360px;font:600 16px "Montserrat",sans-serif;letter-spacing:5px;color:var(--ink)}
.hero-foot-sub{left:420px;top:658px;width:360px;font-size:12px;color:var(--muted)}
.hero-dots{left:582px;top:700px;display:flex;gap:8px}
.hero-dots span{width:8px;height:8px;border-radius:50%;background:#cfcfcf}
.hero-dots span.on{background:#8c8c8c}
.side-title{left:160px;top:426px;width:200px;font:700 14px "Montserrat",sans-serif;letter-spacing:2px;color:var(--ink)}
.side-copy{left:160px;top:454px;width:200px;font-size:11px;line-height:17px;color:var(--text)}
.tin{left:176px;top:502px;width:170px;height:229px;background:linear-gradient(180deg,#2a2a2a,#111);border-top:6px solid #3a3a3a}
.tin-name{left:176px;top:650px;width:170px;font:400 15px "Montserrat",sans-serif;color:#fff}

/* about */
.eyebrow{font:400 12px "Montserrat",sans-serif;letter-spacing:4px;color:var(--muted)}
.section-title{font:600 27px "Montserrat",sans-serif;letter-spacing:6px;color:var(--ink)}
.title-rule{width:130px;height:2px;background:var(--rule)}
.lead{font-size:13px;line-height:24px;color:var(--text)}
.cta{left:475px;top:938px;width:250px;height:42px;background:var(--pink);color:#fff;display:flex;align-items:center;justify-content:center;gap:28px;font:600 12px "Montserrat",sans-serif;letter-spacing:3px}
.free-badge{left:790px;top:978px;width:112px;height:112px;border-radius:50%;background:#f7f7f7;border:2px dashed #c9c9c9;display:flex;flex-direction:column;align-items:center;justify-content:center;color:var(--ink)}
.free-badge .f-small{font-size:9px;line-height:12px}
.free-badge .f-big{font:400 26px "Playfair Display",serif;line-height:30px}
.free-badge .f-foot{font-size:9px;line-height:12px;color:var(--pink)}
.divider{top:1018px;height:1px;background:var(--rule)}

/* featured */
.product{top:1220px;width:276px}
.product .cat{font:600 18px "Montserrat",sans-serif;letter-spacing:3px;color:var(--ink);text-align:center;height:41px}
.product .photo{height:260px;position:relative}
.product .name{margin-top:24px;text-align:center;font-size:17px;color:var(--ink)}
.product .price{margin-top:6px;text-align:center;font-size:12px;color:var(--pink)}
.photo.cake{background:radial-gradient(circle at 45% 55%,#f8f0dc 0%,#e8d1a2 45%,#b9a07a 100%)}
.photo.macaron{background:linear-gradient(180deg,#3b3333,#1e1a1a)}
.photo.cookie{background:radial-gradient(circle at 50% 45%,#6e3f26 0%,#4a2616 55%,#b88d6c 100%)}
.photo.gelato{background:radial-gradient(circle at 50% 55%,#f5d9b0 0%,#efc9ca 45%,#f7f2f2 100%)}
.overlay{position:absolute;inset:0;display:flex;flex-direction:column;align-items:center;padding-top:80px;color:#fff}
.overlay .t{font:600 18px "Montserrat",sans-serif;letter-spacing:3px}
.overlay .s{margin-top:4px;font:400 12px "Montserrat",sans-serif;letter-spacing:3px;text-decoration:underline}
.overlay .btns{margin-top:48px;display:flex;gap:12px}
.overlay .btns span{width:40px;height:40px;border:1px solid #fff;display:flex;align-items:center;justify-content:center}
.overlay .btns span.hot{background:var(--pink);border-color:var(--pink)}

/* newsletter */
.join{left:0;top:1643px;width:1200px;height:123px;background:var(--mint)}
.join-label{left:172px;top:1694px;font:700 18px "Montserrat",sans-serif;letter-spacing:2px;color:var(--ink)}
.join-label span{font-weight:400}
.join-input{left:484px;top:1676px;width:230px;height:56px;background:#fff;font-size:13px;color:var(--muted);display:flex;align-items:center;padding-left:22px}
.join-go{left:714px;top:1676px;width:50px;height:56px;background:var(--pink);display:flex;align-items:center;justify-content:center}
.social{top:1643px;width:76px;height:123px;background:var(--mint-deep);display:flex;flex-direction:column;align-items:center;justify-content:center;gap:8px;font:600 9px "Montserrat",sans-serif;letter-spacing:1px;color:#fff}
.social .sq{width:14px;height:14px;background:#fff}
.quote{left:0;top:1808px;width:1200px;font:400 26px "Montserrat",sans-serif;color:var(--ink)}
.quote b{font-weight:700}
.quote-sub{left:0;top:1852px;width:1200px;font-size:13px;color:var(--text)}

/* footer */
.footer{left:0;top:1920px;width:1200px;height:592px;background:var(--footer)}
.f-head{font:700 12px "Montserrat",sans-serif;letter-spacing:1px;color:#fff}
.f-list{list-style:none;margin-top:10px}
.f-list li{font-size:10px;line-height:19px;color:var(--footer-text)}
.f-list li::before{content:"";display:inline-block;width:4px;height:4px;background:#fff;border-radius:50%;margin-right:10px;vertical-align:middle}
.f-text{font-size:10px;line-height:17px;color:var(--footer-text)}
.f-tel{left:173px;top:2346px;font:400 28px "Montserrat",sans-serif;color:#fff}
.f-brand{left:795px;top:1986px;display:flex;align-items:center;gap:20px;font:400 22px "Montserrat",sans-serif;color:#fff}
.f-brand .mark{width:54px;height:54px;border-radius:50%;background:#fff}
.gallery{left:795px;top:2090px;width:236px;height:212px;display:grid;grid-template-columns:repeat(3,1fr);gap:4px}
.gallery div{background:#7d7068}
.gallery div:nth-child(2n){background:#4a413d}
.gallery div:nth-child(3n){background:#bdb0a6}
.f-cart{left:950px;top:2352px;display:flex;align-items:center;gap:6px;font:700 11px "Montserrat",sans-serif;letter-spacing:1px;color:#fff}
.f-cart .count{width:18px;height:18px;border-radius:50%;background:var(--pink);font-size:10px;display:flex;align-items:center;justify-content:center;letter-spacing:0}
.f-delivery{left:522px;top:2290px;width:180px;height:36px;background:var(--mint);border:2px solid #fff;display:flex;align-items:center;justify-content:center;font:700 12px "Montserrat",sans-serif;letter-spacing:3px;color:var(--ink)}
.f-delivery-note{left:522px;top:2332px;width:180px;font-size:10px;color:#fff}
.copyright{left:0;top:2438px;width:1200px;font-size:11px;color:#8a8a8a}
.copyright a{color:#8a8a8a;text-decoration:underline}
</style>
</head>
<body>

<!-- header -->
<div class="abs delivery-tag">FREE DELIVERY</div>
<div class="abs delivery-note center">For Order Above $80</div>
<div class="abs brand-mark"></div>
<div class="abs brand-name center">Lantern &amp; Plum</div>
<div class="abs call">Call: 020-5550 1846</div>
<svg class="abs search" width="16" height="16" viewBox="0 0 16 16"><circle cx="6.5" cy="6.5" r="5" fill="none" stroke="#1d1d1d" stroke-width="1.6"/><line x1="10.2" y1="10.2" x2="15" y2="15" stroke="#1d1d1d" stroke-width="1.6"/></svg>
<div class="abs login">LOGIN</div>
<div class="abs signup">SIGNUP</div>
<div class="abs cart">
  <svg width="16" height="14" viewBox="0 0 16 14"><path d="M1 1h3l2 8h8l1.5-6H5" fill="none" stroke="#1d1d1d" stroke-width="1.5"/><circle cx="7" cy="12" r="1.3" fill="#1d1d1d"/><circle cx="13" cy="12" r="1.3" fill="#1d1d1d"/></svg>
  <span class="count">0</span>CART
</div>
<nav class="abs main-nav">
  <span class="active">HOME</span><span class="sep">/</span><span>CAKES</span><span class="sep">/</span><span>MACARONS</span><span class="sep">/</span><span>COOKIES</span><span class="sep">/</span><span>GELATO</span><span class="sep">/</span><span>TASTING ROOM</span><span class="sep">/</span><span>ABOUT US</span>
</nav>
<div class="abs nav-rule"></div>

<!-- hero -->
<div class="abs hero" role="img" aria-label="Soft pink studio backdrop with pastries"></div>
<div class="abs hero-tart" role="img" aria-label="Cream tart topped with chocolate drizzle"></div>
<div class="abs hero-kicker center">LANTERN</div>
<div class="abs hero-title center">GELATO</div>
<div class="abs hero-sub center">Nullam molestie</div>
<div class="abs hero-badge">
  <div class="b-top">PREMIUM</div>
  <div class="b-script">Quality</div>
  <div class="b-main">PASTRY</div>
  <div class="b-sub">sweet dessert</div>
</div>
<div class="abs hero-foot center">NATURAL INGREDIENTS</div>
<div class="abs hero-foot-sub center">not add preservatives</div>
<div class="abs hero-dots"><span class="on"></span><span></span><span></span></div>
<div class="abs side-title center">SEMPER AUCTOR</div>
<div class="abs side-copy center">Imperdiet quam mi quis justo.<br>Etiam a massa sed leo.</div>
<div class="abs tin" role="img" aria-label="Black gift tin of pastries"></div>
<div class="abs tin-name center">Lantern &amp; Plum</div>

<!-- about -->
<div class="abs eyebrow center" style="left:0;top:778px;width:1200px">ABOUT</div>
<h2 class="abs section-title center" style="left:0;top:798px;width:1200px">WE VALUE FLAVOR</h2>
<div class="abs title-rule" style="left:535px;top:846px"></div>
<p class="abs lead center" style="left:250px;top:862px;width:700px">Nullam molestie, nulla eu blandit ullamcorper, lorem nunc dictum purus, vitae imperdiet quam mi quis justo. Etiam a massa dignissim fringilla. Suspendisse potenvamus pellentes molestie eu tincidunt sapien dictum.</p>
<div class="abs cta">TAKE THE FIRST BITE
  <svg width="16" height="10" viewBox="0 0 16 10"><path d="M0 5h14M10 1l4 4-4 4" fill="none" stroke="#fff" stroke-width="1.6"/></svg>
</div>
<div class="abs divider" style="left:0;width:790px"></div>
<div class="abs divider" style="left:902px;width:298px"></div>
<div class="abs free-badge">
  <div class="f-small">Get a</div>
  <div class="f-big">free</div>
  <div class="f-small">food tasting</div>
  <div class="f-foot">try now</div>
</div>

<!-- featured -->
<div class="abs eyebrow center" style="left:0;top:1052px;width:1200px">ABOUT</div>
<h2 class="abs section-title center" style="left:0;top:1072px;width:1200px">FEATURED</h2>
<div class="abs title-rule" style="left:535px;top:1120px"></div>
<p class="abs lead center" style="left:250px;top:1136px;width:700px">Nullam molestie, nulla eu blandit ullamcorper, lorem nunc dictum purus, vitae imperdiet quam mi quis justo. Etiam a massa dignissim fringilla. Suspendisse potenvamus pellentes molestie eu tincidunt sapien dictum.</p>

<div class="abs product" style="left:25px">
  <div class="cat">CAKES</div>
  <div class="photo cake" role="img" aria-label="Cream cake with fresh fruit"></div>
  <div class="name">Nullam molestie purus</div>
  <div class="price">$9.00 only</div>
</div>
<div class="abs product" style="left:317px">
  <div class="cat">MACARONS</div>
  <div class="photo macaron" role="img" aria-label="Macarons on a dark plate">
    <div class="overlay">
      <div class="t">QUIER MACARONS</div>
      <div class="s">ETIAM AUCTOR</div>
      <div class="btns">
        <span><svg width="14" height="14" viewBox="0 0 14 14"><path d="M6 8l2-2M5 6L3 8a2 2 0 003 3l2-2M9 8l2-2a2 2 0 00-3-3L6 5" fill="none" stroke="#fff" stroke-width="1.3"/></svg></span>
        <span class="hot"><svg width="14" height="14" viewBox="0 0 14 14"><path d="M7 12S1 8 1 4.5A3 3 0 017 3a3 3 0 016 1.5C13 8 7 12 7 12z" fill="#fff"/></svg></span>
        <span><svg width="16" height="14" viewBox="0 0 16 14"><path d="M1 1h3l2 8h8l1.5-6H5" fill="none" stroke="#fff" stroke-width="1.4"/><circle cx="7" cy="12" r="1.2" fill="#fff"/><circle cx="13" cy="12" r="1.2" fill="#fff"/></svg></span>
      </div>
    </div>
  </div>
  <div class="name">Monserisque mare frnare</div>
  <div class="price">$4.00 only</div>
</div>
<div class="abs product" style="left:608px">
  <div class="cat">COOKIES</div>
  <div class="photo cookie" role="img" aria-label="Chocolate layer cake with curls"></div>
  <div class="name">Nullam molestie purus</div>
  <div class="price">$6.00 only</div>
</div>
<div class="abs product" style="left:899px">
  <div class="cat">GELATO</div>
  <div class="photo gelato" role="img" aria-label="Ice cream sandwich with macaron shells"></div>
  <div class="name">Monserisque mare frnare</div>
  <div class="price">$12.00 only</div>
</div>

<!-- newsletter -->
<div class="abs join"></div>
<div class="abs join-label">JOIN US <span>FOR PROIN CONVAL</span></div>
<div class="abs join-input">Type Your Email Here</div>
<div class="abs join-go"><svg width="16" height="10" viewBox="0 0 16 10"><path d="M0 5h14M10 1l4 4-4 4" fill="none" stroke="#fff" stroke-width="1.6"/></svg></div>
<div class="abs social" style="left:798px"><span class="sq"></span>LIKE US</div>
<div class="abs social" style="left:874px;background:#95c9be"><span class="sq"></span>FOLLOW US</div>
<div class="abs social" style="left:950px"><span class="sq"></span>JOIN US</div>

<div class="abs quote center">Quser <b>orcitae</b> eros posuere semper metus.</div>
<div class="abs quote-sub center">Morbi varius nisi ac dolor cursus quis lacus vitae enim dapibus laoreet. Donec iaculis, metus non.</div>

<!-- footer -->
<footer class="abs footer"></footer>
<div class="abs" style="left:173px;top:1976px">
  <div class="f-head">CAKES.</div>
  <ul class="f-list"><li>Fresh cream cakes</li><li>Seasonal fruit tarts</li><li>Chocolate layer cake</li><li>Cheesecake slices</li></ul>
</div>
<div class="abs" style="left:324px;top:1976px">
  <div class="f-head">COOKIES.</div>
  <ul class="f-list"><li>Butter shortbread</li><li>Almond crunch cookies</li><li>Double chocolate chip</li></ul>
</div>
<div class="abs" style="left:173px;top:2094px">
  <div class="f-head">MACARONS.</div>
  <ul class="f-list"><li>Rose and lychee</li><li>Salted caramel macaron</li><li>Pistachio cream</li><li>Gift boxes of twelve</li></ul>
</div>
<div class="abs" style="left:324px;top:2094px">
  <div class="f-head">GELATO.</div>
  <ul class="f-list"><li>Vanilla bean gelato</li><li>Dark cocoa sorbet</li><li>Mango and passionfruit</li></ul>
</div>
<div class="abs" style="left:522px;top:1976px">
  <div class="f-head">CUSTOMER SERVICES.</div>
  <ul class="f-list"><li>Contact Us</li><li>Shipping</li><li>FAQs</li></ul>
</div>
<div class="abs" style="left:522px;top:2094px">
  <div class="f-head">ABOUT US.</div>
  <ul class="f-list"><li>Our Story</li><li>Our Chefs</li><li>Tasting Room</li></ul>
</div>
<div class="abs" style="left:173px;top:2240px;width:280px">
  <div class="f-head">LANTERN &amp; PLUM.</div>
  <p class="f-text" style="margin-top:10px">Unit 12, Harbour Road, Tianhe District,<br>Guangzhou, China 510000</p>
  <p class="f-text" style="margin-top:6px;text-decoration:underline">hello@lanternandplum.com</p>
</div>
<div class="abs f-tel">Tel: 020-5550 1846</div>
<div class="abs f-head" style="left:522px;top:2240px;text-decoration:underline">QUESTION?</div>
<div class="abs f-delivery">FREE DELIVERY</div>
<div class="abs f-delivery-note center">For Order Above $80</div>
<div class="abs f-brand"><span class="mark"></span>Lantern &amp; Plum</div>
<div class="abs gallery" role="img" aria-label="Grid of pastry photos">
  <div></div><div></div><div></div><div></div><div></div><div></div><div></div><div></div><div></div>
</div>
<div class="abs f-cart">
  <svg width="16" height="14" viewBox="0 0 16 14"><path d="M1 1h3l2 8h8l1.5-6H5" fill="none" stroke="#fff" stroke-width="1.5"/><circle cx="7" cy="12" r="1.3" fill="#fff"/><circle cx="13" cy="12" r="1.3" fill="#fff"/></svg>
  <span class="count">0</span>CART
</div>
<div class="abs copyright center">© Copyright 2015 <a>www.lanternandplum.com</a>. All Rights Reserved.</div>

</body>
</html>
```